Private Investigative Business Needs Brochure Design

I need a highly professional and contemporary brochure for a new private investigative business I own. I am a retired detective with 35 years of investigative experience. I am looking to obtain all types of clients, with a primary focus on law firms, attorneys, insurance companies, businesses, schools, elderly, families and individuals . I have a web site to use to get more information on what I am doing and seeking, Thanks very much! Much of the content I will use can come from my website www.BranwickPI.com. I may want to add or change a pic or two once I see the results from the design experts. Hope that is ok
Updates

I am sorry for the late changes but most of them are simply cut and paste from the below information. I reworded some of the information I currently have on my website. If possible I am seeking a brochure design that includes some of the pics I already posted along with the below information. Please let me know if you have any questions and thank you to all for your great design work. My spacing and font is not correct and needs your expertise as well.I do appreciate it!• Branwick Investigative Services, LLC President, Tom Branwick is a former Captain with the Coastal State Patrol and Chief of Detectives with a county prosecutor’s office. Tom has 35 years of investigative experience. • No, we don’t offer bodyguards, drones, or conduct polygraphs, but the investigative services we offer you we are among the very best at conducting.• Our experience has taught us how to operate in tightly scripted environments, paying strict attention to applicable laws. We conduct the finest private investigations without invading anyone’s privacy, and we meticulously avoid steps-even if legal- that may not be in your best interest. Our results will stand up to the harshest of scrutiny by judges, juries, attorneys, the media and the public. • Branwick Investigative Services, LLC specializes in helping litigators-across all areas of practice-succeed in depositions, trials, and negotiations. We are skilled at finding admissible evidence that is often hidden through various means or reluctant witnesses.Tom Branwick is President of Branwick Investigative Services, LLC. He is a former executive officer with 35 years of law enforcement and investigative experience. He obtained the rank of Captain with the Coastal State Patrol (retired) and Chief of Detectives with the Ellisford County Prosecutor’s Office during his extensive law enforcement career.His experience with the Coastal State Patrol included assignment to and supervision of numerous investigative units that included:• Special Projects/Auto Unit • Official Corruption Unit • High Technology Crimes and Investigative Support Unit (Unit Leader) • Special Investigations and Services Bureau (Bureau Chief)• Polygraph Unit • TRACE Unit (homicide tracking) • Special Investigations Unit (Background Investigations) • Riverbend Athletic Grounds Unit • Alcohol Beverage Control Unit • Internal Affairs and Investigations Bureau• Office of Professional Standards (Bureau Chief) Tom has a vast amount of experience successfully investigating high profile criminal cases that included, homicides, aggravated assaults, missing persons, sexual assaults, white collar crimes, political corruption, official misconduct, Internet frauds, corporate frauds, identity thefts, burglaries, bank robberies, manufacturer/distribution of child pornography, conspiracy and much more. In addition, he was instrumental in the creation and oversight of numerous highly successful multi agency investigative task forces that included: • Coastal State Patrol Statewide Computer Crimes Task Force • Coastal State Patrol Cyber Terrorism Task Force • Online Offenses Youth Protection Task Force (OOYP)• Coastal State Patrol Upper District Corruption Task Force Upon retirement from the Coastal State Patrol Tom continued his law enforcement and investigative career as a detective assigned to the Major Crimes Unit for the Ellisford County Prosecutor’s Office. Within two years Tom was promoted from the rank of detective to the Chief of Detectives, a position he held for several years. He had oversight over all major crimes within the county, while working with municipal, county, state, and federal law enforcement agencies. As Chief of Detectives he was instrumental in the supervision of a multi-agency task force that successfully investigated and arrested a serial killer responsible for the murder and attempted murder of numerous women along the East Coast. He helped implement and supervise their first county Computer Crimes Unit, Intelligence Unit and Office of Professional Standards Units. He also oversaw the counties Roadway Fatality Response Group (RFRG) and created the ECPO School Safety County Task Force. Tom is a graduate of Oakvale County Community College and Pembrook Ashford University, obtaining an Associate’s Degree in Criminal Justice and a Bachelor’s Degree in Business Administration. He is also a graduate of Castlemere University, School of Police Staff and Command. Branwick Investigative Services, LLC has extensive investigative and analytical resources available to assist with the most complex of civil investigations. Our investigative staff includes former detectives with decades of experience with the Coastal State Patrol. In addition, we have highly skilled intelligence analysts available to assist us with investigations and your needs. We welcome any questions you may have about Branwick Investigative Services, LLC and will gladly provide references. We will work tirelessly to get the job done for you, always in an ethical, legal and professional way. We are confident that if you use Branwick Investigative Services, LLC one time, you will use us every time!www.BranwickPI.com (4) Please cut and paste the below under Attorney ServicesHurley Investigative Services, LLC specializes in assessing the validity of civil litigation cases, particularly when you need to determine the merit and veracity of your client’s claims. With 35 years of experience investigating criminal and civil cases we can save you significant money, time and resources throughout the litigation process, especially when you need the best factual information available prior to setting in motion a full scale litigation. Tom Branwick has conducted thousands of interviews of witnesses, victims, defendants and complainants. Tom’s investigative experience enables him to be able to conduct professional, ethical, and affordable investigations for litigation cases that include: Motor Vehicle Accidents, Wrongful Deaths, Premises Liability, Nursing Home and Elder Abuse, Civil Rights, Corporate Fraud and more. He will always represent your firm, business and you in the highest of standards and always with your best interests in mind. (5) Please cut and paste the below under Corporate Fraud InvestigationsDuring the past few years we have seen a dramatic increase in the types and volume of corporate fraud committed. Corporate fraud can be committed by employees from part-time to high level management and CEO’s of major corporations. Corporate fraud can occur in any type of business, from a small family owned one to a major corporation. If you have been the victim of corporate fraud you know the significant impact it can have on your business, finances and employee morale. Companies victimized by fraud often times find themselves exposed to unwanted publicity and media coverage that can cause irrefutable damage. Tom Branwick, President of Branwick Investigative Services, LLC has an extensive background investigating corporate and public sector fraud, corruption, theft and embezzlement cases. We know how to operate in tightly scripted environments, paying strict attention to the law, internal policies and procedures, without bringing unwanted attention to you. With decades of investigative experience comes the ability to prepare reports that are professional, meticulously written, factually correct and understandable. Our reports and testimony withstand the scrutiny of the judges, juries, attorneys, media, individuals and the test of time. In addition, Branwick Investigative Services, LLC offers consultations on how to improve retail security, reduce shrinkage from theft and implement policies and procedures to limit potential litigation. If you believe you may be the victim of corporate fraud we can perform a critical and independent assessment of the validity and strength of the evidence, culminating in a detailed exhaustive report of findings. (6) Please cut and paste the below under Accidental and Personal Injury ReconstructionHurley Investigative Services, LLC conducts thorough accident reconstruction investigations to determine the cause of the accident so you can make an informed decision. We work with attorneys, adjusters, insurance companies, and individuals involved in all types of accidents. As an independent investigator it is our duty to analyze the cause of the accident so that liability and/or financial responsibility can be resolved. It is very likely that during your lifetime you or a family member will be involved in some type of accident. You may be required to defend your actions, provide a deposition to insurance companies or become a litigant as a result of the accident not being your fault. The best decision is to do it with the assistance of Branwick Investigative Services, LLC.(7) Please cut and paste the below under Background Investigations” (change checks to investigations)Branwick Investigative Services, LLC provides in-depth background investigations on individuals including: pre- employment, nanny, caretaker for the elderly and more. We focus on attention to detail and thoroughness, while always conducting our investigations in a legal and ethical manner. Our comprehensive background investigation and detailed report gives you understandable, information and intelligence that helps you make the most informed decision. We utilize on-line sources, open sources, proprietary databases and information developed through interviewing and intelligence seeking the best assessment of the indivuduals reputation with your best interest always a priority. Added Thursday, April 9, 2015

Target Market(s)

Law firms, attorneys, insurance companies, businesses, education, elderly and individuals

Industry/Entity Type

Detective

Font styles to use
Sans Serif
Decorative
Script

Colors
3277b5
ffffff
33a6d7
ec1f27
85cae6
fbf289
cadf82
d3a5cc

Requirements
Must have
• Highly professional appearance, contemporary coloring, pic's that I included. In addition it is my background (bio) that is a major marketing tool that I would like placed early on.
Nice to have
• Something out of the box, primary target is attorneys and law firms
Should not have
• any typical private detective pictures

```html
<!DOCTYPE html>
<html lang="en">
<head>
<meta charset="utf-8">
<title>Branwick Investigative Services – Brochure</title>
<link href="https://fonts.googleapis.com/css2?family=Roboto:wght@400;500;700&display=swap" rel="stylesheet">
<style>
  :root {
    --page: #eeeff1;
    --navy: #1d4c8a;
    --blue: #3277b5;
    --sky: #33a6d7;
    --pale: #85cae6;
    --ink: #1d1d1f;
    --paper: #ffffff;
    --mist: #e3e6ea;
    --gold: #c9a13a;
    --red: #ec1f27;
  }
  * { box-sizing: border-box; margin: 0; padding: 0; }
  html, body { width: 1200px; height: 997px; overflow: hidden; }
  body { background: var(--page); font-family: "Roboto", Arial, sans-serif; color: var(--ink); }

  .brochure {
    position: absolute; left: 30px; top: 44px; width: 1140px; height: 910px;
    background: var(--paper); box-shadow: 0 4px 18px rgba(0,0,0,.18); overflow: hidden;
  }
  .brochure-backdrop { position: absolute; inset: 0; }
  .fold { position: absolute; top: 0; bottom: 0; width: 1px; background: rgba(0,0,0,.12); }
  .fold--one { left: 380px; } .fold--two { left: 760px; }

  .placeholder { position: absolute; }

  /* left panel */
  .brand { position: absolute; left: 22px; top: 14px; width: 340px; }
  .brand-name { display: flex; align-items: center; gap: 10px; font-weight: 700; font-size: 46px; color: #2b2b2e; line-height: 1; }
  .brand-mark { width: 34px; height: 34px; background: var(--blue); }
  .brand-sub { font-size: 20px; font-weight: 500; color: #2b2b2e; margin-top: 4px; padding-left: 44px; }
  .brand-tag { font-size: 13px; font-weight: 700; color: var(--navy); margin-top: 2px; padding-left: 10px; }
  .image-strip { left: 0; top: 116px; width: 380px; height: 178px;
    background: linear-gradient(90deg, #2f9fa3 0%, #a9d9da 45%, #f2f2f2 60%, #7fa4c6 78%, #1d3b3b 100%); }
  .intro { position: absolute; left: 20px; top: 318px; width: 340px; font-size: 16.5px; line-height: 1.22; color: #1d1d1f; }
  .intro strong { font-weight: 700; }
  .gavel { left: 24px; top: 548px; width: 110px; height: 80px; border-radius: 8px;
    background: linear-gradient(135deg, #f1d27a 0%, #c99a3a 55%, #9a6f1e 100%); opacity: .9; }
  .contact { position: absolute; left: 28px; top: 712px; color: var(--paper); font-size: 13.5px; line-height: 1.32; font-style: normal; }
  .contact-phone { font-size: 19px; margin-bottom: 2px; }

  /* badges */
  .badge { position: absolute; display: flex; align-items: center; }
  .badge-tab { width: 120px; height: 16px; border-radius: 4px; background: linear-gradient(#e9f5fc, #5fb7e2); border: 2px solid var(--sky); }
  .badge-circle { width: 132px; height: 132px; border-radius: 50%; background: var(--blue);
    border: 5px solid var(--sky); box-shadow: 0 0 0 3px #cfeaf7; display: flex; align-items: center; justify-content: center;
    text-align: center; color: var(--paper); font-weight: 700; font-size: 24px; line-height: 1.12; margin-left: -6px; }
  .badge--contact { left: 200px; top: 600px; }
  .badge--contact .badge-tab { width: 40px; }
  .badge--about { left: 460px; top: 352px; }
  .badge--experience { left: 596px; top: 40px; }
  .badge--experience .badge-tab { width: 48px; }
  .badge--experience .badge-circle { width: 124px; height: 124px; font-size: 22px; }

  /* middle panel */
  .binoculars { left: 398px; top: 26px; width: 180px; height: 86px; border-radius: 12px;
    background: linear-gradient(90deg, #2a2a2e 0%, #2f6fc4 30%, #2a2a2e 50%, #2f6fc4 70%, #2a2a2e 100%); opacity: .85; }
  .fraud-lens { left: 392px; top: 196px; width: 140px; height: 130px; border-radius: 10px;
    background: linear-gradient(135deg, #8fdc6a 0%, #2e8a2e 60%, #1c5b1d 100%); }
  .scales { left: 570px; top: 184px; width: 170px; height: 160px; border-radius: 10px;
    background: linear-gradient(180deg, rgba(243,210,124,.85) 0%, rgba(184,138,44,.75) 100%); }
  .about-list { position: absolute; left: 398px; top: 496px; width: 350px; list-style: none; color: var(--paper); font-size: 14.8px; line-height: 1.2; }
  .about-list li { position: relative; padding-left: 18px; margin-bottom: 12px; }
  .about-list li::before { content: ""; position: absolute; left: 2px; top: 6px; width: 7px; height: 7px; border-radius: 50%; background: var(--paper); }
  .about-list li.lead { text-align: center; }
  .silhouettes { left: 440px; top: 820px; width: 300px; height: 90px;
    background: linear-gradient(180deg, rgba(20,50,90,0) 0%, rgba(20,40,80,.75) 60%, rgba(15,35,70,.9) 100%); }

  /* right panel */
  .experience { position: absolute; left: 776px; top: 18px; width: 352px; color: var(--paper); font-size: 14.2px; line-height: 1.24; }
  .experience p { margin-bottom: 9px; }
  .unit-list { list-style: none; margin-bottom: 10px; }
  .unit-list li { position: relative; padding-left: 11px; }
  .unit-list li::before { content: "•"; position: absolute; left: 0; }
  .crest { left: 1010px; top: 70px; width: 110px; height: 150px; border-radius: 12px; background: rgba(255,255,255,.06); }
</style>
</head>
<body>
<main class="brochure">
  <svg class="brochure-backdrop" width="1140" height="910" viewBox="0 0 1140 910" aria-hidden="true">
    <defs>
      <linearGradient id="deepBlue" x1="0" y1="0" x2="1" y2="1">
        <stop offset="0" stop-color="#3a86c4"/>
        <stop offset="0.55" stop-color="#2a66a8"/>
        <stop offset="1" stop-color="#1d4c8a"/>
      </linearGradient>
    </defs>
    <rect x="0" y="294" width="380" height="616" fill="#e3e6ea"/>
    <path d="M650,0 C530,150 480,330 380,470 C300,585 150,605 0,700 L0,910 L1140,910 L1140,0 Z" fill="url(#deepBlue)"/>
    <path d="M630,0 C512,150 462,330 362,470 C282,580 140,598 0,688" fill="none" stroke="#85cae6" stroke-width="3" opacity=".7"/>
  </svg>
  <div class="fold fold--one"></div>
  <div class="fold fold--two"></div>

  <section class="panel panel--intro">
    <div class="brand">
      <div class="brand-name"><span class="brand-mark"></span>Branwick</div>
      <div class="brand-sub">Investigative Services</div>
      <div class="brand-tag">35 Years of Investigative Excellence!</div>
    </div>
    <div class="placeholder image-strip" role="img" aria-label="Collage of cyber crime, magnifying glass over binary code, close-up of an eye and identity theft word cloud"></div>
    <p class="intro"><strong>Branwick Investigative Services, LLC</strong> is a full service, private investigative agency that is licensed and bonded in the state of Coastal State. Located in central Coastal State we provide a complete array of investigative services. With 35 years of investigative and law enforcement experience we deliver professional results, ethically, confidentially, and with attention to detail.</p>
    <div class="placeholder gavel" role="img" aria-label="Photo of a gold judge's gavel"></div>
    <div class="badge badge--contact"><span class="badge-tab"></span><span class="badge-circle">Contact<br>Us</span></div>
    <address class="contact">
      <div class="contact-phone">Phone: 555-318-0472</div>
      Branwick Investigative Services<br>
      P.O. Box 40217<br>
      Maple Harbor, Coastal State<br>
      04190<br>
      Email: TomBranwickPI@mailhub.net<br>
      Web: http://www.branwickpi.com
    </address>
  </section>

  <section class="panel panel--about">
    <div class="placeholder binoculars" role="img" aria-label="Photo of black binoculars with blue lenses"></div>
    <div class="placeholder fraud-lens" role="img" aria-label="Photo of a magnifying glass over the word fraud on green binary code"></div>
    <div class="placeholder scales" role="img" aria-label="Photo of golden scales of justice"></div>
    <div class="badge badge--about"><span class="badge-tab"></span><span class="badge-circle">About<br>Us</span></div>
    <ul class="about-list">
      <li class="lead">Branwick Investigative Services, LLC President, Tom Branwick is a former Captain with the Coastal State Patrol and Chief of Detectives with a county prosecutor’s office.</li>
      <li>No, we don’t offer bodyguards, drones, or conduct polygraphs, but the investigative services we offer you we are among the very best at conducting.</li>
      <li>Our experience has taught us how to operate in tightly scripted environments, paying strict attention to applicable laws.</li>
      <li>Branwick Investigative Services, LLC specializes in helping litigators-across all areas of practice-succeed in depositions, trials, and negotiations. We are skilled at finding admissible evidence that is often hidden through various means or reluctant witnesses.</li>
    </ul>
    <div class="placeholder silhouettes" role="img" aria-label="Silhouettes of business people seated around a meeting table"></div>
    <div class="badge badge--experience"><span class="badge-tab"></span><span class="badge-circle">His<br>Experience</span></div>
  </section>

  <section class="panel panel--experience">
    <div class="placeholder crest" role="img" aria-label="Faint police shield decoration"></div>
    <div class="experience">
      <p>Tom Branwick is President of Branwick Investigative Services, LLC. He is a former executive officer with 35 years of law enforcement and investigative experience. He obtained the rank of Captain with the Coastal State Patrol (retired) and Chief of Detectives with the Ellisford County Prosecutor’s Office during his extensive law enforcement career. His experience with the Coastal State Patrol included assignment to and supervision of numerous investigative units that included:</p>
      <ul class="unit-list">
        <li>Special Projects/Auto Unit</li>
        <li>Official Corruption Unit</li>
        <li>High Technology Crimes and Investigative Support Unit (Unit Leader)</li>
        <li>Special Investigations and Services Bureau (Bureau Chief)</li>
        <li>Polygraph Unit • TRACE Unit (homicide tracking)</li>
        <li>Special Investigations Unit (Background Investigations)</li>
        <li>Riverbend Athletic Grounds Unit</li>
        <li>Alcohol Beverage Control Unit</li>
        <li>Internal Affairs and Investigations Bureau</li>
        <li>Office of Professional Standards (Bureau Chief).</li>
      </ul>
      <p>Tom has a vast amount of experience successfully investigating high profile criminal cases that included, homicides, aggravated assaults, missing persons, sexual assaults, white collar crimes, political corruption, official misconduct, Internet frauds, corporate frauds, identity thefts, burglaries, bank robberies, manufacturer/distribution of child pornography, conspiracy and much more. In addition, he was instrumental in the creation and oversight of numerous highly successful multi agency investigative task forces that included:</p>
      <ul class="unit-list">
        <li>Coastal State Patrol Statewide Computer Crimes Task Force</li>
        <li>Coastal State Patrol Cyber Terrorism Task Force</li>
        <li>Online Offenses Youth Protection Task Force (OOYP)</li>
        <li>Coastal State Patrol Upper District Corruption Task Force</li>
      </ul>
    </div>
  </section>
</main>
</body>
</html>
```